The Willow Hours - a modern wellness brand

Looking for a modern, simple, and clean website for a virtual consulting firm focused on holistic wellness and sustainable living. Want a strong combo of text and photos (really shitty starts are available for reference on www.thewillowhours.com and www.helenabrusco.com for reference - general idea is in the right direction, was too difficult to work through with the wordpress template and nothing laid out correctly)
Needs include:
- strong home / landing page
- ability to schedule (use calend.ly) on the site
- online shop / purchasing POS integration
- blog
-multiple 'services' pages
- about page
- contact page
(attached brand board images for brand style / reference)
Updates
Want more opportunity for designs and feedback
Target Market(s)
women and gay men aged 30-50
Coding
Coded - Design and coding required
Number of Pages Required
5+ page
Colors
Designer to choose only greyscale colors for use in the design.
Requirements
Must have
- the ability for me to update and manage through wordpress when things like pricing, or services change
Should not have
- complicated anything

```html
<!DOCTYPE html>
<html lang="en">
<head>
<meta charset="utf-8">
<title>The Willow Hours</title>
<link href="https://fonts.googleapis.com/css2?family=Marcellus&family=Jost:wght@300;400&display=swap" rel="stylesheet">
<style>
:root{
  --ink:#1f211d;
  --text:#2b2b2b;
  --muted:#6b6b6b;
  --beige:#ebe1d6;
  --soft:#f8f8f8;
  --line:#d9d9d9;
  --plum:#2a1a47;
  --white:#ffffff;
}
*{margin:0;padding:0;box-sizing:border-box}
html,body{width:1200px;height:4286px;overflow:hidden;background:var(--white)}
body{position:relative;font-family:"Jost",sans-serif;font-weight:300;color:var(--text)}
.abs{position:absolute}
.heading{font-family:"Marcellus",serif;font-weight:400;color:var(--ink);text-transform:uppercase}
.btn{position:absolute;display:flex;align-items:center;justify-content:center;background:var(--ink);color:var(--white);font-family:"Jost",sans-serif;font-weight:400;font-size:20px;text-transform:uppercase;text-decoration:none}
.center{left:0;width:1200px;text-align:center}

/* header */
.brand{left:111px;top:28px;display:flex;align-items:center;gap:18px}
.brand-dot{width:60px;height:60px;border:2px solid var(--ink);border-radius:50%}
.brand-name{font-family:"Marcellus",serif;font-size:24px;letter-spacing:4px;color:var(--ink);text-transform:uppercase;white-space:nowrap}
.nav{left:566px;top:44px;display:flex;gap:30px;font-size:17px;font-weight:400;text-transform:uppercase;color:var(--text)}
.nav .active{text-decoration:underline;text-underline-offset:5px}

/* hero */
.hero-title{left:111px;top:204px;font-size:64px;line-height:76px}
.hero-sub{left:111px;top:374px;width:400px;font-size:24px;line-height:36px;color:#444}
.hero-photo{left:569px;top:113px;width:532px;height:532px;border-radius:50%;background:radial-gradient(circle at 40% 40%,#d8d8d8,#9a9a9a 70%,#7a7a7a)}

/* welcome */
.welcome{left:0;top:710px;width:1200px;height:566px;background:var(--beige)}
.welcome-title{left:614px;top:792px;font-size:43px;line-height:47px}
.welcome-text{left:614px;top:906px;width:486px;font-size:17px;line-height:31px;color:#3a3a3a}

/* focus */
.section-title{font-size:42px;line-height:50px}
.focus-photo{top:1433px;width:468px;height:314px}
.focus-caption{top:1768px;width:468px;text-align:center;font-size:27px;font-weight:300;color:var(--text)}

/* process */
.process{left:0;top:1909px;width:1200px;height:526px;background:var(--soft)}
.step-num{width:80px;text-align:center;font-size:36px;color:#444}
.step-label{width:220px;text-align:center;font-size:22px;font-weight:300}
.step-text{width:220px;text-align:center;font-size:16px;line-height:26px;color:var(--muted)}

/* work */
.work-photo{left:83px;top:2604px;width:599px;height:391px;background:linear-gradient(160deg,#f2f2f2,#cfcfcf 70%,#e6e6e6)}
.work-kicker{left:741px;top:2584px;font-size:25px;font-weight:300}
.work-title{left:741px;top:2636px;width:370px;font-size:31px;line-height:38px;font-family:"Jost",sans-serif;font-weight:300;text-transform:uppercase;color:var(--ink)}
.work-text{left:741px;top:2730px;width:360px;font-size:17px;line-height:27px;color:var(--muted)}

/* blog */
.blog{left:0;top:3058px;width:1200px;height:603px;background:var(--soft)}
.post{top:3210px;width:308px}
.post-photo{width:308px;height:216px}
.post-title{margin-top:16px;font-size:22px;font-weight:300;color:var(--text)}
.post-date{margin-top:6px;font-size:15px;color:var(--muted);display:flex;align-items:center;gap:6px}
.post-text{margin-top:20px;font-size:17px;line-height:26px;color:var(--muted)}

/* footer */
.footer{left:0;top:3919px;width:1200px;height:367px;background:var(--plum)}
.footer-brand{left:128px;top:4020px;display:flex;align-items:center;gap:16px}
.footer-brand .ring{width:40px;height:40px;border:2px solid var(--white);border-radius:50%}
.footer-brand span{font-family:"Marcellus",serif;font-size:28px;line-height:34px;letter-spacing:3px;color:var(--white);text-transform:uppercase}
.footer-links{left:503px;top:3970px;list-style:none;font-size:18px;line-height:30px;font-weight:400;color:var(--white)}
.footer-contact{left:742px;top:3970px;font-size:18px;line-height:30px;font-weight:400;color:var(--white)}
.footer-contact div{display:flex;align-items:center;gap:6px}
.social{top:4060px;width:40px;height:40px;border-radius:50%;background:var(--white)}
.footer-rule{left:111px;top:4215px;width:978px;height:1px;background:rgba(255,255,255,.25)}
.copyright{top:4240px;font-size:17px;font-weight:400;color:var(--white)}
</style>
</head>
<body>

<!-- header -->
<div class="abs brand"><div class="brand-dot"></div><div class="brand-name">The Willow Hours</div></div>
<nav class="abs nav"><span class="active">Home</span><span>About</span><span>Services</span><span>Blog</span><span>Contact</span></nav>
<a class="btn" style="left:1003px;top:35px;width:85px;height:43px;font-size:17px">Shop</a>

<!-- hero -->
<h1 class="abs heading hero-title">The Willow<br>Hours</h1>
<p class="abs hero-sub">We focused on holistic wellness and sustainable living.</p>
<a class="btn" style="left:111px;top:479px;width:175px;height:62px">Schedule</a>
<svg class="abs" style="left:549px;top:93px" width="572" height="572" viewBox="0 0 572 572" aria-hidden="true">
  <circle cx="286" cy="286" r="282" fill="none" stroke="var(--plum)" stroke-width="10" stroke-dasharray="0 28" stroke-linecap="round"/>
</svg>
<div class="abs hero-photo" role="img" aria-label="Black and white photo of wildflowers in a meadow with a hand reaching through"></div>

<!-- welcome -->
<section class="abs welcome"></section>
<h2 class="abs heading welcome-title">Welcome to<br>The Willow Hours</h2>
<p class="abs welcome-text">Lorem ipsum dolor sit amet, consectetur adipiscing elit, sed do eiusmod tempor incididunt ut labore et dolore magna aliqua. Ut enim ad minim veniam, quis nostrud exercitation ullamco laboris nisi ut aliquip ex ea commodo consequat. Duis aute irure dolor in reprehenderit in voluptate velit esse cillum dolore eu fugiat nulla pariatur teur sint occaecat cupidatat.</p>
<a class="btn" style="left:616px;top:1130px;width:156px;height:56px">Read More</a>

<!-- focus -->
<h2 class="abs heading section-title center" style="top:1340px">We Focus On</h2>
<div class="abs focus-photo" style="left:111px;background:linear-gradient(180deg,#e4e4e4 0%,#bdbdbd 45%,#6e6e6e 100%)" role="img" aria-label="Man with open arms standing in a wheat field"></div>
<div class="abs focus-photo" style="left:621px;background:linear-gradient(135deg,#4a4a4a,#2e2e2e 60%,#3c3c3c)" role="img" aria-label="Aerial view of a dense forest canopy"></div>
<div class="abs focus-caption" style="left:111px">Holistic Wellness</div>
<div class="abs focus-caption" style="left:621px">Sustainable Living</div>

<!-- process -->
<section class="abs process"></section>
<h2 class="abs heading section-title center" style="top:1972px">Our Process</h2>
<svg class="abs" style="left:0;top:2060px" width="1200" height="320" viewBox="0 2060 1200 320" aria-hidden="true">
  <path d="M113 2218 A120 120 0 0 1 353 2218 A120 120 0 0 0 593 2218 A120 120 0 0 1 833 2218 A120 120 0 0 0 1073 2218" fill="none" stroke="var(--line)" stroke-width="3"/>
  <g fill="none" stroke="var(--plum)" stroke-width="3" stroke-linecap="round">
    <circle cx="233" cy="2150" r="14"/><path d="M227 2166 h12 M228 2172 h10"/>
    <path d="M233 2124 v-6 M212 2132 l-5 -4 M254 2132 l5 -4 M205 2150 h-6 M261 2150 h6"/>
    <path d="M198 2208 c0 -18 16 -28 35 -28 c19 0 35 10 35 28 z"/>
    <circle cx="452" cy="2263" r="12"/><path d="M430 2300 c0 -14 10 -22 22 -22 c12 0 22 8 22 22 z"/>
    <rect x="478" y="2215" width="42" height="26" rx="13"/><circle cx="478" cy="2252" r="4"/><circle cx="470" cy="2262" r="2.5"/>
    <path d="M692 2210 c-6 -10 -8 -20 -4 -32 c6 -18 24 -26 40 -20 c14 6 20 18 18 30 l-2 10 l6 6 h-8 v10 h-10 v12"/>
    <circle cx="718" cy="2184" r="8"/><circle cx="718" cy="2184" r="15" stroke-dasharray="5 4"/>
    <circle cx="742" cy="2160" r="5"/>
    <path d="M920 2290 h60 v-60 h-15 v15 h-15 v15 h-15 v15 h-15 z M935 2290 v-15 h45 M950 2290 v-30 h30 M965 2290 v-45"/>
  </g>
</svg>
<div class="abs step-num" style="left:193px;top:2048px">1</div>
<div class="abs step-label" style="left:123px;top:2230px">Understand</div>
<div class="abs step-text" style="left:123px;top:2276px">Duis aute irure dolor in rep reherderit in voluptate velit esse cillum dolore</div>
<div class="abs step-text" style="left:363px;top:2074px">Duis aute irure dolor in rep reherderit in voluptate velit esse cillum dolore</div>
<div class="abs step-label" style="left:363px;top:2166px">Imagine</div>
<div class="abs step-num" style="left:433px;top:2332px">2</div>
<div class="abs step-num" style="left:672px;top:2048px">3</div>
<div class="abs step-label" style="left:602px;top:2230px">Create</div>
<div class="abs step-text" style="left:602px;top:2276px">Duis aute irure dolor in rep reherderit in voluptate velit esse cillum dolore</div>
<div class="abs step-text" style="left:843px;top:2074px">Duis aute irure dolor in rep reherderit in voluptate velit esse cillum dolore</div>
<div class="abs step-label" style="left:843px;top:2174px">Built</div>
<div class="abs step-num" style="left:913px;top:2332px">4</div>

<!-- work -->
<h2 class="abs heading section-title center" style="top:2500px">Our Work</h2>
<div class="abs work-photo" role="img" aria-label="Printed brochure cover with the brand name, lying at an angle"></div>
<div class="abs work-kicker">The Willow Hours</div>
<h3 class="abs work-title">Executive &amp; Individual Coaching</h3>
<p class="abs work-text">Lorem ipsum dolor sit amet, consectetur adipi scing elit, sed do eiusmod tempor incididuntt labore et dolore magna aliquatrst enim adilm veniam, quis nostrud exerci.</p>
<a class="btn" style="left:741px;top:2869px;width:156px;height:55px">Shop Now</a>

<!-- blog -->
<section class="abs blog"></section>
<h2 class="abs heading section-title center" style="top:3122px">Our Blog</h2>
<article class="abs post" style="left:111px">
  <div class="post-photo" style="background:linear-gradient(180deg,#d6d6d6,#bcbcbc 60%,#8a8a8a)" role="img" aria-label="Person walking alone on a misty beach"></div>
  <div class="post-title">Finibus Bonorum et Malorum</div>
  <div class="post-date"><svg width="13" height="13" viewBox="0 0 13 13"><rect x="1" y="2" width="11" height="10" fill="none" stroke="currentColor"/><path d="M1 5h11M4 0v3M9 0v3" stroke="currentColor"/></svg>23/10/2022</div>
  <p class="post-text">Duis aute irure dolor in reprehenderit in voluptate velit esse cillum dolore eu fugiat nulla pariatur.</p>
</article>
<article class="abs post" style="left:446px">
  <div class="post-photo" style="background:linear-gradient(180deg,#cfcfcf,#9b9b9b 55%,#6a6a6a)" role="img" aria-label="Woman with raised arms standing in a lake at sunset"></div>
  <div class="post-title">Finibus Bonorum et Malorum</div>
  <div class="post-date"><svg width="13" height="13" viewBox="0 0 13 13"><rect x="1" y="2" width="11" height="10" fill="none" stroke="currentColor"/><path d="M1 5h11M4 0v3M9 0v3" stroke="currentColor"/></svg>23/10/2022</div>
  <p class="post-text">Duis aute irure dolor in reprehenderit in voluptate velit esse cillum dolore eu fugiat nulla pariatur.</p>
</article>
<article class="abs post" style="left:782px">
  <div class="post-photo" style="background:linear-gradient(135deg,#5a5a5a,#9e9e9e 50%,#d0d0d0)" role="img" aria-label="Smiling woman holding a stack of pebbles"></div>
  <div class="post-title">Finibus Bonorum et Malorum</div>
  <div class="post-date"><svg width="13" height="13" viewBox="0 0 13 13"><rect x="1" y="2" width="11" height="10" fill="none" stroke="currentColor"/><path d="M1 5h11M4 0v3M9 0v3" stroke="currentColor"/></svg>23/10/2022</div>
  <p class="post-text">Duis aute irure dolor in reprehenderit in voluptate velit esse cillum dolore eu fugiat nulla pariatur.</p>
</article>

<!-- call to action -->
<h2 class="abs heading center" style="top:3726px;font-size:40px">Let’s Work Together.</h2>
<a class="btn" style="left:521px;top:3797px;width:158px;height:60px">Contact Us</a>

<!-- footer -->
<footer class="abs footer"></footer>
<div class="abs footer-brand"><div class="ring"></div><span>The Willow<br>Hours</span></div>
<ul class="abs footer-links">
  <li>Home</li><li>About</li><li>Services</li><li>Blog</li><li>Contact</li><li>Privacy Policy</li><li>Terms &amp; Conditions</li>
</ul>
<div class="abs footer-contact">
  <div><svg width="15" height="15" viewBox="0 0 16 16"><path d="M3 1l3 3-2 2c1 2 3 4 5 5l2-2 3 3-2 3C6 15 1 10 1 3z" fill="currentColor"/></svg>1 555 014 2288</div>
  <div><svg width="16" height="12" viewBox="0 0 16 12"><rect width="16" height="12" fill="currentColor"/><path d="M0 0l8 7 8-7" fill="none" stroke="var(--plum)" stroke-width="1.5"/></svg>info@thewillowhours.com</div>
</div>
<div class="abs social" style="left:740px"></div>
<div class="abs social" style="left:784px"></div>
<div class="abs social" style="left:829px"></div>
<div class="abs footer-rule"></div>
<div class="abs copyright center">© Copyright 2022 The Willow Hours- All rights reserved.</div>

</body>
</html>
```